Maple Lantern Business Card

Design of business cards

Target Market(s)

We are aiming as small business owners who need anything from basic business structures, website plans, business processes and quality assurance.

Industry/Entity Type

Business

Colors

Designer to choose colors to be used in the design.

Requirements
Nice to have
• I would prefer one side of the card to use the green from the logo. Prefer to have the same font as the logo.

```html
<!DOCTYPE html>
<html lang="en">
<head>
<meta charset="utf-8">
<title>Maple Lantern Consulting – Business Card</title>
<link rel="stylesheet" href="https://fonts.googleapis.com/css2?family=Ubuntu:wght@400;500&display=swap">
<style>
  :root {
    --paper-light: #e9e7e4;
    --paper-dark: #d6d6d7;
    --brand-green: #8dc63f;
    --leaf-deep: #5fa85a;
    --mint: #55c39a;
    --lime: #c8cc55;
    --coral: #e8304a;
    --rose: #e9607a;
    --ink: #1b1b1b;
    --text-grey: #4a4a4a;
    --white: #ffffff;
  }
  * { box-sizing: border-box; margin: 0; padding: 0; }
  html, body { width: 741px; height: 1200px; overflow: hidden; }
  body { font-family: "Ubuntu", sans-serif; background: var(--paper-dark); }

  .card { position: relative; width: 741px; height: 1200px; overflow: hidden; }
  .card__backdrop { position: absolute; inset: 0; width: 741px; height: 1200px; }

  .brand { position: absolute; left: 46px; top: 108px; display: flex; align-items: center; gap: 20px; }
  .brand__dot { width: 84px; height: 84px; border-radius: 50%; background: var(--brand-green); }
  .brand__name {
    color: var(--brand-green); font-weight: 500; font-size: 31px; line-height: 1.2;
    letter-spacing: 1.5px; text-transform: uppercase;
  }

  .contact { position: absolute; display: flex; align-items: center; gap: 38px; }
  .contact__badge { width: 82px; height: 82px; flex: none; }
  .contact__text { color: var(--text-grey); font-size: 33px; font-weight: 400; white-space: nowrap; }
  .contact--name  { left: 44px;  top: 379px; }
  .contact--email { left: 109px; top: 492px; }
  .contact--phone { left: 176px; top: 603px; }
  .contact--chat  { left: 242px; top: 718px; }
  .contact--chat .contact__text { font-size: 29px; }
</style>
</head>
<body>
<main class="card">
  <svg class="card__backdrop" viewBox="0 0 741 1200" aria-hidden="false">
    <defs>
      <linearGradient id="paper" x1="0" y1="0" x2="1" y2="1">
        <stop offset="0" stop-color="var(--paper-light)"/>
        <stop offset="1" stop-color="var(--paper-dark)"/>
      </linearGradient>
      <linearGradient id="greenFacet" x1="0" y1="0" x2="1" y2="1">
        <stop offset="0" stop-color="var(--lime)"/>
        <stop offset="0.45" stop-color="var(--brand-green)"/>
        <stop offset="0.75" stop-color="var(--mint)"/>
        <stop offset="1" stop-color="var(--leaf-deep)"/>
      </linearGradient>
      <linearGradient id="redFacet" x1="0" y1="0" x2="1" y2="1">
        <stop offset="0" stop-color="#ee5a3c"/>
        <stop offset="0.5" stop-color="var(--coral)"/>
        <stop offset="1" stop-color="var(--rose)"/>
      </linearGradient>
    </defs>
    <rect width="741" height="1200" fill="url(#paper)"/>
    <polygon points="395,0 741,0 741,611" fill="url(#greenFacet)" role="img" aria-label="Green faceted triangle mosaic"/>
    <polygon points="0,574 361,1200 0,1200" fill="url(#redFacet)" role="img" aria-label="Red and pink faceted triangle mosaic"/>
  </svg>

  <header class="brand">
    <span class="brand__dot"></span>
    <h1 class="brand__name">Maple Lantern<br>Consulting</h1>
  </header>

  <div class="contact contact--name">
    <svg class="contact__badge" viewBox="0 0 82 82" aria-hidden="true">
      <circle cx="41" cy="41" r="41" fill="var(--brand-green)"/>
      <circle cx="41" cy="41" r="34" fill="none" stroke="var(--white)" stroke-width="1.5" stroke-dasharray="4 3"/>
      <g fill="var(--white)" stroke="var(--white)" stroke-width="3" stroke-linecap="round">
        <line x1="29" y1="29" x2="53" y2="53"/>
        <line x1="53" y1="29" x2="29" y2="53"/>
        <polygon points="23,23 35,24 24,35" stroke-width="1"/>
        <polygon points="59,23 47,24 58,35" stroke-width="1"/>
        <polygon points="23,59 35,58 24,47" stroke-width="1"/>
        <polygon points="59,59 47,58 58,47" stroke-width="1"/>
      </g>
    </svg>
    <span class="contact__text">YOUR NAME HERE</span>
  </div>

  <div class="contact contact--email">
    <svg class="contact__badge" viewBox="0 0 82 82" aria-hidden="true">
      <circle cx="41" cy="41" r="41" fill="var(--ink)"/>
      <circle cx="41" cy="41" r="34" fill="none" stroke="var(--white)" stroke-width="1.5" stroke-dasharray="4 3"/>
      <rect x="24" y="29" width="34" height="24" fill="var(--white)"/>
      <polyline points="24,29 41,43 58,29" fill="none" stroke="var(--ink)" stroke-width="2"/>
    </svg>
    <span class="contact__text">hello@maplelantern.net</span>
  </div>

  <div class="contact contact--phone">
    <svg class="contact__badge" viewBox="0 0 82 82" aria-hidden="true">
      <circle cx="41" cy="41" r="41" fill="var(--coral)"/>
      <circle cx="41" cy="41" r="34" fill="none" stroke="var(--white)" stroke-width="1.5" stroke-dasharray="4 3"/>
      <path d="M31 24 l6 -2 l4 9 l-4 3 q3 8 9 12 l3 -4 l9 4 l-2 6 q-4 3 -10 0 q-13 -8 -17 -20 q-1 -5 2 -8z" fill="var(--white)"/>
    </svg>
    <span class="contact__text">+10 555 018 2046</span>
  </div>

  <div class="contact contact--chat">
    <svg class="contact__badge" viewBox="0 0 82 82" aria-hidden="true">
      <circle cx="41" cy="41" r="41" fill="var(--ink)"/>
      <circle cx="41" cy="41" r="34" fill="none" stroke="var(--white)" stroke-width="1.5" stroke-dasharray="4 3"/>
      <path d="M24 27 h34 a3 3 0 0 1 3 3 v17 a3 3 0 0 1 -3 3 h-20 l-8 7 v-7 h-6 a3 3 0 0 1 -3 -3 v-17 a3 3 0 0 1 3 -3z" fill="var(--white)"/>
    </svg>
    <span class="contact__text">YOUR CHAT ACCOUNT</span>
  </div>
</main>
</body>
</html>
```